Brackwater Vale Medical Website to make connecting and communicating easier

To create a unique, user-friendly, professional website for patients and professionals to access education/ information, forms, appointments, contact details, and data about us, and for us to have the capacity to link to various cloud-based platforms.
To use the logo design and colour scheme we have just sourced.

WEBSITE to be eye catching, Inspiring and alluring
- efficient and logical
- professional and trustworthy appearance
- health focus "living health matters"
- user friendly
- ability to link with cloud-based software and video conferencing tools/ telehealth
- colours- black/ white teal and ?silver

PAGES:
page 1 - Our clinic and staff, services offered, contact us- address/ map / contact details- social media connections
page 2- patients and visitors - New patient forms to complete, news and patient informtion (educatinal)
page 3 - health professionals -referral forms, research and education
page 3- online appointments
page 4 - Quick links - partners, other services
page 5- privacy policy, disclaimer

Need extra days to review

HI, Could we please extend the deadline another 5 days, so sorry just struggling with my workload to be able to keep up and I am wanting to liaise more with the designer that I will choose. I am so happy with PixelForge and all the designers - thank you! Thank you so much!!

Target Market(s)

Patients - mostly over 60's so the website must be minimal clicks and simple to navigate
Professionals - for education and access forms

Industry/Entity Type

Health Care

Coding

Coded - Design and coding required

Number of Pages Required

5+ page

Font styles to use
Sans Serif
Script

Colors
33b8a4
86cfc6

Requirements
Must have
• WEBSITE to be eye catching, Inspiring and alluring
- efficient and logical
- user friendly

WEBSITE - professional and user friendly
- ability to link with cloud based software and videoconferencing/ telehealth
Nice to have
• clean and crisp presentation
happy for an innovative look
room to add more services and ability to link pages and resources
Should not have
• Please ensure the website is not:
clunky
difficult to navigate
common and cheap looking

```html
<!DOCTYPE html>
<html lang="en">
<head>
<meta charset="utf-8">
<title>Brackwater Vale Medical</title>
<link href="https://fonts.googleapis.com/css2?family=Arvo:wght@400;700&family=Archivo+Black&family=Poppins:wght@300;400;500;600&display=swap" rel="stylesheet">
<style>
:root{
  --teal:#33b8a4;
  --teal-light:#86cfc6;
  --teal-deep:#2aa592;
  --dark:#25292b;
  --dark-2:#1c2022;
  --ink:#2b2b2b;
  --muted:#7a7a7a;
  --line:#dcdcdc;
  --paper:#ffffff;
  --mist:#f3f4f4;
}
*{margin:0;padding:0;box-sizing:border-box}
html,body{width:1200px;height:4093px;overflow:hidden;background:var(--paper)}
body{position:relative;font-family:'Poppins',sans-serif;color:var(--ink)}
.abs{position:absolute}
.serif{font-family:'Arvo',serif}
.photo{position:absolute;display:block}
.btn{position:absolute;display:flex;align-items:center;justify-content:center;background:var(--teal);color:#fff;border-radius:22px;font-family:'Arvo',serif;font-size:13px;letter-spacing:.3px}
.eyebrow{position:absolute;left:0;width:1200px;text-align:center;font-family:'Arvo',serif;color:var(--teal);font-size:16px}
.title{position:absolute;left:0;width:1200px;text-align:center;font-family:'Arvo',serif;font-size:32px;color:var(--ink)}
.body-text{font-size:12px;line-height:20px;color:var(--muted)}

/* header */
.topbar{position:absolute;top:0;left:0;width:1200px;height:32px}
.topbar-teal{position:absolute;top:0;left:326px;right:0;height:32px;background:var(--teal);clip-path:polygon(22px 0,100% 0,100% 100%,0 100%)}
.topbar-text{position:absolute;top:0;height:32px;display:flex;align-items:center;color:#fff;font-size:11px}
.navbar{position:absolute;top:32px;left:0;width:1200px;height:73px;background:rgba(40,44,46,.88)}
.logo{position:absolute;left:64px;top:41px;font-family:'Arvo',serif;font-size:19px;line-height:25px;color:#fff;text-align:center}
.nav{position:absolute;top:32px;height:73px;display:flex;align-items:center;font-size:11.5px;color:#fff}
.nav a{position:absolute;white-space:nowrap;color:#fff;text-decoration:none}
.nav a.active{color:var(--teal)}
.nav-underline{position:absolute;left:290px;top:101px;width:46px;height:3px;background:var(--teal)}

/* hero */
.hero-photo{left:0;top:0;width:1200px;height:715px;background:linear-gradient(100deg,#e8e4e0 0%,#d9d3cd 30%,#b9b6b3 48%,#3d4b52 62%,#9aa8ad 78%,#d4c8bf 100%)}
.hero-kicker{position:absolute;left:80px;top:287px;font-family:'Arvo',serif;font-size:18px;color:var(--ink)}
.hero-title{position:absolute;left:77px;top:320px;font-family:'Archivo Black',sans-serif;font-size:41px;line-height:49px;color:#111;letter-spacing:.5px}
.hero-title .accent{color:var(--teal)}

/* feature cards */
.feature{position:absolute;top:974px;width:254px;height:254px;background:#fff;box-shadow:0 2px 12px rgba(0,0,0,.12);text-align:center}
.feature .ring{position:absolute;left:85px;top:44px;width:84px;height:84px;border-radius:50%;border:2px solid var(--teal);display:flex;align-items:center;justify-content:center}
.feature .ring span{width:72px;height:72px;border-radius:50%;background:var(--teal);display:flex;align-items:center;justify-content:center}
.feature h3{position:absolute;top:154px;left:0;width:100%;font-family:'Arvo',serif;font-weight:400;font-size:15px;color:var(--ink)}
.feature p{position:absolute;top:180px;left:26px;width:202px;font-size:10.5px;line-height:19px;color:var(--muted)}

/* about */
.about-bg{left:0;top:1109px;width:1200px;height:592px;background:linear-gradient(120deg,#2c3336 0%,#1f2527 45%,#2a3134 100%)}
.about-text{position:absolute;left:663px;width:320px}

/* services */
.service{position:absolute;top:1835px;width:251px;height:347px;background:#fff;box-shadow:0 1px 10px rgba(0,0,0,.1)}
.service .pic{position:absolute;left:0;top:0;width:251px;height:170px}
.service .badge{position:absolute;left:28px;top:102px;width:56px;height:56px;border-radius:50%;background:#fff;border:2px solid var(--teal);display:flex;align-items:center;justify-content:center}
.service h3{position:absolute;left:24px;top:204px;font-family:'Arvo',serif;font-weight:400;font-size:15px}
.service p{position:absolute;left:21px;top:232px;width:214px;font-size:10.5px;line-height:19.5px;color:var(--muted)}
.service .more{position:absolute;right:24px;top:318px;font-size:11px;color:var(--teal)}

/* why us */
.why-bg{left:0;top:2290px;width:1200px;height:391px;background:var(--mist)}
.why-item{position:absolute;top:2479px;width:180px;text-align:center}
.why-item .icon{margin:0 auto;width:96px;height:96px;border-radius:50%;background:#fff;box-shadow:0 2px 8px rgba(0,0,0,.08);display:flex;align-items:center;justify-content:center}
.why-item .icon.active{border:2px solid var(--teal-light)}
.why-item p{margin-top:18px;font-family:'Arvo',serif;font-size:13.5px;color:var(--ink)}

/* team */
.team-bg{position:absolute;left:0;top:2681px;width:1200px;height:600px;background:linear-gradient(180deg,#33b8a4 0%,#3bbcaa 100%)}
.staff{position:absolute;top:2860px;width:226px;height:305px;background:#fff;text-align:center}
.staff .pic{position:absolute;left:8px;top:8px;width:210px;height:215px}
.staff h4{position:absolute;top:252px;left:0;width:100%;font-family:'Arvo',serif;font-weight:400;font-size:15px}
.staff span{position:absolute;top:274px;left:0;width:100%;font-size:12px;color:var(--muted)}
.social-strip{position:absolute;left:40px;top:189px;display:flex;gap:4px}
.social-strip i{width:34px;height:34px;background:var(--teal);display:flex;align-items:center;justify-content:center}

/* contact */
.field{position:absolute;height:30px;border-bottom:1px solid var(--line);font-size:10px;color:#555;padding-top:2px}
.field.focus{border-bottom:2px solid var(--teal-light)}

/* footer */
.footer{position:absolute;left:0;top:3785px;width:1200px;height:264px;background:var(--dark)}
.footer h4{position:absolute;top:59px;font-family:'Arvo',serif;font-weight:400;font-size:17px;color:#fff}
.footer .txt{position:absolute;font-size:11px;line-height:20px;color:#c9cccd}
.foot-ico{position:absolute;width:18px;height:18px}
.bottombar{position:absolute;left:0;top:4049px;width:1200px;height:44px;background:var(--dark-2)}
.bottombar-teal{position:absolute;left:0;top:0;width:875px;height:44px;background:var(--teal);clip-path:polygon(0 0,100% 0,calc(100% - 26px) 100%,0 100%)}
</style>
</head>
<body>

<!-- HERO -->
<div class="photo hero-photo" role="img" aria-label="Patient on a video call with a doctor shown on a laptop screen in a bright living room"></div>
<svg class="abs" style="left:0;top:660px" width="1200" height="60" viewBox="0 0 1200 60" preserveAspectRatio="none"><path d="M0 56 Q600 -30 1200 56 L1200 60 L0 60Z" fill="#fff"/></svg>

<header>
  <div class="topbar">
    <div class="topbar-teal"></div>
    <div class="topbar-text" style="left:724px">24 / 7 hour Services :</div>
    <svg class="abs" style="left:857px;top:4px" width="24" height="24" viewBox="0 0 24 24"><circle cx="12" cy="12" r="11" fill="none" stroke="#fff" stroke-width="1.5"/><path d="M8.5 7.5l2 0 1 2.5-1.3 1a6 6 0 0 0 2.8 2.8l1-1.3 2.5 1 0 2c-4.5.4-8.4-3.5-8-8z" fill="#fff"/></svg>
    <div class="topbar-text serif" style="left:889px;font-size:14px">+1 555 014 7290</div>
    <svg class="abs" style="left:1030px;top:9px" width="13" height="14" viewBox="0 0 13 14"><circle cx="6.5" cy="4" r="3.3" fill="#fff"/><path d="M0 14c0-4 3-6 6.5-6S13 10 13 14z" fill="#fff"/></svg>
    <div class="topbar-text serif" style="left:1051px;font-size:12px">Member Login</div>
  </div>
  <div class="navbar"></div>
  <div class="logo">Brackwater Vale<br>Medical</div>
  <nav class="nav">
    <a class="active" style="left:297px">Home</a>
    <a style="left:353px">About Us</a>
    <a style="left:421px">Our Services</a>
    <a style="left:513px">New Patients</a>
    <a style="left:606px">Health Professional</a>
    <a style="left:733px">Online Appointment</a>
    <a style="left:864px">Contact Us</a>
  </nav>
  <div class="nav-underline"></div>
  <div class="btn" style="left:946px;top:49px;width:194px;height:38px">BOOK AN APPOINTMENT</div>
</header>

<section>
  <div class="hero-kicker">We Take Your Health Seriously</div>
  <h1 class="hero-title">WE GENERALLY<br>CARE ABOUT YOUR<br><span class="accent">WELLBEING</span></h1>
  <div class="btn" style="left:81px;top:482px;width:141px;height:39px">CONTACT US</div>
</section>

<!-- WELCOME -->
<section>
  <div class="eyebrow" style="top:752px">Welcome Visitor!</div>
  <h2 class="title" style="top:776px;font-weight:400">Brackwater Vale Medical</h2>
  <p class="abs" style="left:0;top:836px;width:1200px;text-align:center;font-size:12px;color:var(--teal)">We offer complete healthcare to individuals with various health concerns.</p>
  <p class="abs body-text" style="left:360px;top:864px;width:480px;text-align:center">Lorem Ipsum has been the industry's standard dummy text ever since the 1500s, when an unknown printer took a galley of type and scrambled it to make a type specimen book.</p>
</section>

<!-- ABOUT (dark) -->
<div class="photo about-bg" role="img" aria-label="Dark blurred view of medical equipment on a desk"></div>
<svg class="abs" style="left:0;top:1660px" width="1200" height="42" viewBox="0 0 1200 42" preserveAspectRatio="none"><path d="M0 41 Q600 -18 1200 41 L1200 42 L0 42Z" fill="#fff"/></svg>

<div class="feature" style="left:194px">
  <div class="ring"><span><svg width="38" height="38" viewBox="0 0 38 38" fill="none" stroke="#fff" stroke-width="2"><rect x="9" y="6" width="20" height="27" rx="2"/><path d="M15 6v-2h8v2M13 15h12M13 21h12M13 27h8"/></svg></span></div>
  <h3>New Patients</h3>
  <p>Lorem Ipsum has been the industry's standard dummy text look.</p>
</div>
<div class="feature" style="left:472px">
  <div class="ring"><span><svg width="38" height="38" viewBox="0 0 38 38" fill="none" stroke="#fff" stroke-width="2"><rect x="7" y="7" width="24" height="24" rx="4"/><path d="M19 12v14M12 19h14"/></svg></span></div>
  <h3>Health Professional</h3>
  <p>Lorem Ipsum has been the industry's standard dummy text look.</p>
</div>
<div class="feature" style="left:750px">
  <div class="ring"><span><svg width="38" height="38" viewBox="0 0 38 38" fill="none" stroke="#fff" stroke-width="2"><rect x="6" y="9" width="26" height="22" rx="2"/><path d="M6 15h26M12 6v5M26 6v5M11 20h4M17 20h4M23 20h4M11 25h4M17 25h4"/></svg></span></div>
  <h3>Online Appointment</h3>
  <p>Lorem Ipsum has been the industry's standard dummy text look.</p>
</div>

<svg class="abs" style="left:220px;top:1300px" width="360" height="380" viewBox="0 0 360 380">
  <line x1="340" y1="12" x2="30" y2="365" stroke="#33b8a4" stroke-width="18" stroke-linecap="round"/>
  <line x1="300" y1="80" x2="80" y2="330" stroke="#86cfc6" stroke-width="14" stroke-linecap="round" opacity=".7"/>
  <circle cx="182" cy="178" r="160" fill="#33b8a4"/>
</svg>
<div class="photo" style="left:252px;top:1328px;width:300px;height:300px;border-radius:50%;background:linear-gradient(135deg,#eef1f2 0%,#d6dde0 45%,#3f7f9a 75%,#cfd6d8 100%)" role="img" aria-label="Doctor with a tablet consulting a patient in a clinic"></div>

<div class="about-text" style="top:1320px">
  <p class="serif" style="font-size:16px;color:var(--teal)">About Us</p>
  <h2 class="serif" style="margin-top:6px;font-size:31px;font-weight:400;color:#fff">Our Clinic</h2>
  <p class="body-text" style="margin-top:10px;color:#c8cccd">Lorem Ipsum has been the industry's standard dummy text ever since the 1500s, when an unknown printer took a galley of type and scrambled.</p>
  <p class="body-text" style="margin-top:8px;color:#c8cccd">Lorem Ipsum has been the industry's standard dummy text ever since the 1500s, when an unknown printer took a galley of type and scrambled it to make a type specimen book.</p>
</div>
<div class="btn" style="left:663px;top:1565px;width:142px;height:37px">LEARN MORE</div>

<!-- SERVICES -->
<section>
  <div class="eyebrow" style="top:1747px;font-size:13px">What We Do</div>
  <h2 class="title" style="top:1767px;font-weight:400">Our Services</h2>

  <div class="service" style="left:202px">
    <div class="photo pic" style="background:linear-gradient(120deg,#e7e3dc,#c9d6dc 55%,#3e7fb5)" role="img" aria-label="Nurse caring for an elderly patient and a child"></div>
    <svg class="abs" style="left:0;top:140px" width="251" height="32" viewBox="0 0 251 32" preserveAspectRatio="none"><path d="M0 32 Q120 -6 251 10 L251 32Z" fill="#fff"/><path d="M0 30 Q120 -8 251 8" stroke="#33b8a4" stroke-width="3" fill="none"/></svg>
    <div class="badge"><svg width="30" height="30" viewBox="0 0 30 30" fill="none" stroke="#2b2b2b" stroke-width="1.6"><path d="M15 24s-9-5-9-11a4.5 4.5 0 0 1 9-1 4.5 4.5 0 0 1 9 1c0 6-9 11-9 11z"/></svg></div>
    <h3>General Practice</h3>
    <p>Lorem Ipsum has been the industry's standard dummy text ever since the when an unknown printer.</p>
    <div class="more">Learn More —</div>
  </div>
  <div class="service" style="left:475px">
    <div class="photo pic" style="background:linear-gradient(120deg,#cfe0ea,#5b8fc2 50%,#d9c7b9)" role="img" aria-label="Masked clinician attending a patient"></div>
    <svg class="abs" style="left:0;top:140px" width="251" height="32" viewBox="0 0 251 32" preserveAspectRatio="none"><path d="M0 32 Q120 -6 251 10 L251 32Z" fill="#fff"/><path d="M0 30 Q120 -8 251 8" stroke="#33b8a4" stroke-width="3" fill="none"/></svg>
    <div class="badge"><svg width="30" height="30" viewBox="0 0 30 30" fill="none" stroke="#2b2b2b" stroke-width="1.6"><circle cx="15" cy="15" r="7"/><path d="M15 3v5M15 22v5M3 15h5M22 15h5M6.5 6.5l3.5 3.5M20 20l3.5 3.5M23.5 6.5L20 10M10 20l-3.5 3.5"/></svg></div>
    <h3>Covid-19 Service</h3>
    <p>Lorem Ipsum has been the industry's standard dummy text ever since the when an unknown printer.</p>
    <div class="more">Learn More —</div>
  </div>
  <div class="service" style="left:748px">
    <div class="photo pic" style="background:linear-gradient(120deg,#dfe6e4,#9fb9b0 45%,#f0ece6)" role="img" aria-label="Pharmacist talking with a customer at the counter"></div>
    <svg class="abs" style="left:0;top:140px" width="251" height="32" viewBox="0 0 251 32" preserveAspectRatio="none"><path d="M0 32 Q120 -6 251 10 L251 32Z" fill="#fff"/><path d="M0 30 Q120 -8 251 8" stroke="#33b8a4" stroke-width="3" fill="none"/></svg>
    <div class="badge"><svg width="30" height="30" viewBox="0 0 30 30" fill="none" stroke="#2b2b2b" stroke-width="1.6"><rect x="9" y="9" width="12" height="16" rx="2"/><rect x="8" y="4" width="14" height="5" rx="1"/><path d="M15 13v8M11 17h8"/></svg></div>
    <h3>Pharmacy</h3>
    <p>Lorem Ipsum has been the industry's standard dummy text ever since the when an unknown printer.</p>
    <div class="more">Learn More —</div>
  </div>

  <svg class="abs" style="left:535px;top:2218px" width="120" height="30" viewBox="0 0 120 30" fill="none">
    <path d="M14 5 L6 15 L14 25" stroke="#bbb" stroke-width="2"/>
    <circle cx="35" cy="15" r="4" fill="#ccc"/><circle cx="55" cy="15" r="4" fill="#33b8a4"/><circle cx="75" cy="15" r="4" fill="#ccc"/>
    <path d="M100 3 L112 15 L100 27" stroke="#33b8a4" stroke-width="2.5"/>
  </svg>
</section>

<!-- WHY US -->
<div class="photo why-bg"></div>
<div class="photo" style="left:0;top:2296px;width:1200px;height:90px;background:linear-gradient(180deg,#fff 0%,#eceeee 100%)" role="img" aria-label="Faint city skyline silhouette"></div>
<section>
  <p class="abs serif" style="left:90px;top:2462px;font-size:13px;color:var(--teal)">Why Us ?</p>
  <h2 class="abs serif" style="left:88px;top:2488px;font-size:30px;font-weight:400;line-height:38px">Education /<br>Information</h2>
  <div class="btn" style="left:87px;top:2577px;width:195px;height:36px;font-size:12px">BOOK AN APPOINTMENT</div>

  <div class="why-item" style="left:420px"><div class="icon active"><svg width="48" height="48" viewBox="0 0 48 48" fill="none" stroke="#2b2b2b" stroke-width="2"><rect x="10" y="6" width="24" height="34" rx="2"/><path d="M16 16h12M16 22h12M16 28h8"/><path d="M40 10l-12 20-3 4 1-5 12-20z" stroke="#33b8a4"/></svg></div><p>Medical Prescription</p></div>
  <div class="why-item" style="left:603px"><div class="icon"><svg width="48" height="48" viewBox="0 0 48 48" fill="none" stroke="#2b2b2b" stroke-width="2"><rect x="6" y="8" width="36" height="24" rx="2"/><path d="M18 40h12M24 32v8M12 15h4M20 15h14M12 21h4M20 21h14M12 27h4M20 27h10" stroke-width="1.6"/></svg></div><p>Online Education</p></div>
  <div class="why-item" style="left:786px"><div class="icon"><svg width="48" height="48" viewBox="0 0 48 48" fill="none" stroke="#2b2b2b" stroke-width="2"><rect x="6" y="8" width="30" height="26" rx="2"/><path d="M13 28v-6M19 28v-10M25 28v-8M31 28v-13"/><path d="M38 40s-7-4-7-9a3.5 3.5 0 0 1 7-1 3.5 3.5 0 0 1 7 1c0 5-7 9-7 9z" stroke="#33b8a4"/></svg></div><p>Modern Technology</p></div>
  <div class="why-item" style="left:964px"><div class="icon"><svg width="48" height="48" viewBox="0 0 48 48" fill="none" stroke="#2b2b2b" stroke-width="2"><rect x="8" y="6" width="32" height="22" rx="2"/><path d="M21 12v10l8-5z" fill="#33b8a4" stroke="#33b8a4"/><circle cx="14" cy="34" r="3"/><circle cx="24" cy="34" r="3"/><circle cx="34" cy="34" r="3"/><path d="M8 44c0-4 3-6 6-6s6 2 6 6M18 44c0-4 3-6 6-6s6 2 6 6M28 44c0-4 3-6 6-6s6 2 6 6"/></svg></div><p>Webinars</p></div>
</section>

<!-- TEAM -->
<div class="team-bg"></div>
<svg class="abs" style="left:0;top:3235px" width="1200" height="48" viewBox="0 0 1200 48" preserveAspectRatio="none"><path d="M0 48 Q600 -20 1200 48Z" fill="#fff"/></svg>
<section>
  <div class="eyebrow" style="top:2754px;font-size:13px;color:#eafaf7">Meet Our Team</div>
  <h2 class="title" style="top:2780px;font-weight:400;color:#1f3b37">Our Expert Staff</h2>

  <div class="staff" style="left:116px"><div class="photo pic" style="background:linear-gradient(180deg,#eef2f3,#d3dde0)" role="img" aria-label="Portrait of a physiotherapist"></div><h4>Membr Name</h4><span>Phsiotherapist</span></div>
  <div class="staff" style="left:364px"><div class="photo pic" style="background:linear-gradient(180deg,#e9eef0,#cfd9dc)" role="img" aria-label="Portrait of a dentist"></div>
    <div class="social-strip"><i></i><i></i><i></i><i><svg width="14" height="11" viewBox="0 0 14 11" fill="none" stroke="#fff" stroke-width="1.4"><rect x=".7" y=".7" width="12.6" height="9.6"/><path d="M.7 .7l6.3 5 6.3-5"/></svg></i></div>
    <h4>Membr Name</h4><span>Dentist</span></div>
  <div class="staff" style="left:610px"><div class="photo pic" style="background:linear-gradient(180deg,#edf1f2,#d6dfe2)" role="img" aria-label="Portrait of a dermatologist"></div><h4>Membr Name</h4><span style="top:278px">Dermatologyst</span></div>
  <div class="staff" style="left:858px"><div class="photo pic" style="background:linear-gradient(180deg,#eef2f3,#d5dee1)" role="img" aria-label="Portrait of a chiropractor"></div><h4>Membr Name</h4><span>Chiropractist</span></div>
</section>

<!-- CONTACT -->
<section>
  <div class="eyebrow" style="top:3320px;font-size:16px">Contact Us</div>
  <h2 class="title" style="top:3346px;font-weight:400">Request Online Consultation</h2>

  <div class="photo" style="left:113px;top:3429px;width:450px;height:276px;background:linear-gradient(135deg,#eef0f1 0%,#e4e7e9 50%,#edeff0 100%);border:1px solid #e2e2e2" role="img" aria-label="Street map showing the clinic location"></div>

  <div class="field focus" style="left:621px;top:3448px;width:219px">First Name *</div>
  <div class="field" style="left:862px;top:3448px;width:220px">Last Name *</div>
  <div class="field" style="left:621px;top:3496px;width:219px">Enter Email*</div>
  <div class="field" style="left:862px;top:3496px;width:220px">Phone Number *</div>
  <div class="field" style="left:621px;top:3548px;width:219px">Choose Doctor *</div>
  <div class="field" style="left:862px;top:3548px;width:220px">Choose Department *
    <svg class="abs" style="right:8px;top:5px" width="10" height="6" viewBox="0 0 10 6"><path d="M0 0h10L5 6z" fill="#33b8a4"/></svg></div>
  <div class="field" style="left:621px;top:3602px;width:461px;height:48px">Message *
    <svg class="abs" style="right:2px;bottom:3px" width="9" height="9" viewBox="0 0 9 9"><path d="M9 0L0 9M9 4L4 9" stroke="#aaa"/></svg></div>
  <div class="btn" style="left:624px;top:3672px;width:102px;height:35px">SUBMIT</div>
</section>

<!-- FOOTER -->
<footer class="footer">
  <div class="abs" style="left:0;top:0;width:270px;height:3px;background:var(--teal)"></div>
  <h4 style="left:60px;color:var(--teal);font-size:19px;top:56px">Brackwater Vale Medical</h4>
  <p class="txt" style="left:60px;top:90px;width:320px">Lorem Ipsum has been the industry's standard dummy text ever since the 1500s, when an printer took a galley of type and scrambled it Lorem Ipsum has been the text ever since the; when an printer took.</p>
  <svg class="abs" style="left:60px;top:188px" width="100" height="30" viewBox="0 0 100 30" fill="none" stroke="#33b8a4" stroke-width="1.5"><circle cx="14" cy="15" r="13"/><circle cx="50" cy="15" r="13"/><circle cx="86" cy="15" r="13"/></svg>

  <h4 style="left:429px">Contact Us</h4>
  <svg class="foot-ico" style="left:429px;top:100px" viewBox="0 0 18 18" fill="none" stroke="#33b8a4" stroke-width="1.5"><path d="M9 17s-6-6-6-10a6 6 0 0 1 12 0c0 4-6 10-6 10z"/><circle cx="9" cy="7" r="2"/></svg>
  <p class="txt" style="left:466px;top:94px;color:var(--teal)">Brackwater Vale Medical</p>
  <p class="txt" style="left:466px;top:116px;width:230px;line-height:18px">100 – Lorem ipsum text print industry type text printing text.</p>
  <svg class="foot-ico" style="left:429px;top:172px" viewBox="0 0 18 18"><path d="M4 2l3 0 1.5 4-2 1.5a9 9 0 0 0 4 4l1.5-2 4 1.5 0 3C9 15 3 9 4 2z" fill="#33b8a4"/></svg>
  <p class="txt" style="left:466px;top:170px">555 014 7290</p>
  <svg class="foot-ico" style="left:429px;top:203px" viewBox="0 0 18 18"><rect x="1" y="4" width="16" height="11" fill="#33b8a4"/><path d="M1 4l8 6 8-6" stroke="#25292b" stroke-width="1.4" fill="none"/></svg>
  <p class="txt" style="left:466px;top:200px">info@brackwatervale.com</p>

  <h4 style="left:798px">Opening Hours</h4>
  <svg class="foot-ico" style="left:798px;top:101px" viewBox="0 0 18 18" fill="none" stroke="#33b8a4" stroke-width="1.5"><circle cx="9" cy="9" r="7.5"/><path d="M9 4.5V9l3 2"/></svg>
  <p class="txt" style="left:826px;top:99px">Monday - Friday : 9:00 am - 6 :00 pm</p>
  <svg class="foot-ico" style="left:798px;top:133px" viewBox="0 0 18 18" fill="none" stroke="#33b8a4" stroke-width="1.5"><circle cx="9" cy="9" r="7.5"/><path d="M9 4.5V9l3 2"/></svg>
  <p class="txt" style="left:826px;top:131px">Saturday : 9:00 am - 1:00 pm</p>
  <svg class="foot-ico" style="left:798px;top:165px" viewBox="0 0 18 18" fill="none" stroke="#33b8a4" stroke-width="1.5"><circle cx="9" cy="9" r="7.5"/><path d="M9 4.5V9l3 2"/></svg>
  <p class="txt" style="left:826px;top:163px">Sunday : &nbsp;<span style="color:var(--teal)">Closed</span></p>
</footer>
<div class="bottombar">
  <div class="bottombar-teal"></div>
  <p class="abs" style="left:60px;top:14px;font-size:11px;color:#1d3531">©Brackwater Vale Medical - 2020 All rights reserved.</p>
  <p class="abs" style="right:64px;top:14px;font-size:11px;color:#c9cccd">Tearms &amp; Condition &nbsp;| &nbsp;Privacy Policy</p>
</div>

</body>
</html>
```